Sales brochure to promote delivery services

we need new revamped marketing brochure
We are a 3rd Party Logistics company specializing in home delivery and assembly for the home furnishings market. our company provides delivery services, we provide trained delivery teams, we also provide online order tracking, we provide routing and dispatching, expert handling of merchandise, white glove service. the brochure is going to be used for sales dept to leave/mail to potential customers. brochure is intended to give information about our services and attract business.

Target Market(s)

home furniture retailers, furniture and appliance retailers, retailers that require delivery services

Industry/Entity Type

Delivery Service

Requirements
Must have
• color scheme coordinates with company logo
• phone number 415.273-6150 and website address www.bravecrest-3pl.com
Nice to have
• tri-fold design preferred
• include artwork and/or pictures related to our services examples would be dining room, living room, bedroom furniture, kitchen appliances, laundry, white box delivery truck, happy customers

```html
<!DOCTYPE html>
<html lang="en">
<head>
<meta charset="utf-8">
<title>Bravecrest 3PL – Home Delivery & Assembly Brochure</title>
<link href="https://fonts.googleapis.com/css2?family=Montserrat:wght@500;700;800;900&family=Open+Sans:wght@400;600;700&display=swap" rel="stylesheet">
<style>
:root{
  --navy:#2f2f5c;
  --lime:#b9c22b;
  --white:#ffffff;
  --grey:#e7e7ec;
  --ink:#33334f;
  --stage:#ececef;
}
*{box-sizing:border-box;margin:0;padding:0}
html,body{width:800px;height:1200px;overflow:hidden}
body{background:var(--stage);font-family:"Open Sans",Arial,sans-serif;color:var(--ink);position:relative}
.spread{position:absolute;left:20px;width:760px;height:545px;display:grid;grid-template-columns:repeat(3,1fr);box-shadow:0 4px 14px rgba(0,0,0,.18);background:var(--white);overflow:hidden}
.spread--outer{top:28px}
.spread--inner{top:625px}
.panel{position:relative;overflow:hidden;border-right:1px solid var(--grey)}
.panel:last-child{border-right:none}
.swoosh{position:absolute;left:0;width:100%;pointer-events:none}
.dark{background:var(--navy);color:var(--white)}
h2,h3{font-family:"Montserrat",Arial,sans-serif}
.ticks{list-style:none}
.ticks li{position:relative;padding-left:16px;font-size:10px;line-height:1.35;margin-bottom:6px}
.ticks li::before{content:"";position:absolute;left:0;top:3px;width:9px;height:6px;border-left:2.5px solid var(--lime);border-bottom:2.5px solid var(--lime);transform:rotate(-45deg)}
.photo{position:absolute;background:linear-gradient(135deg,#c9c7cf,#8f8ea4)}
.brand{display:flex;align-items:center;gap:6px;font-family:"Montserrat",Arial,sans-serif;font-weight:800;font-size:13px;letter-spacing:.5px;color:var(--white)}
.brand .dot{width:12px;height:12px;border-radius:50%;background:var(--lime)}
.brand--navy{color:var(--navy)}
.web{display:flex;align-items:center;gap:6px;font-size:10px;font-weight:700}
.web svg{flex:none}

/* outer: left */
.o-left .intro{position:absolute;top:0;left:0;right:0;height:205px;padding:22px 20px 0}
.o-left .intro p{font-size:11px;line-height:1.45;margin-bottom:14px}
.o-left .team{position:absolute;top:232px;left:20px;right:18px}
.o-left .team h3{font-size:10px;font-weight:700;color:var(--navy);margin-bottom:8px}
.o-left .help{position:absolute;top:372px;left:20px;right:20px;color:var(--navy)}
.o-left .help .small{font-family:"Montserrat",Arial,sans-serif;font-size:14px;font-weight:800}
.o-left .help .big{font-family:"Montserrat",Arial,sans-serif;font-size:30px;font-weight:900;line-height:1;color:var(--lime)}
.o-left .help .under{font-family:"Montserrat",Arial,sans-serif;font-size:18px;font-weight:800}
.o-left .foot{position:absolute;bottom:0;left:0;right:0;height:48px;padding:20px 0 0 22px;color:var(--white)}

/* outer: middle */
.o-mid .top{position:absolute;top:0;left:0;right:0;height:250px;padding:22px 20px 0;text-align:center}
.o-mid .top p{font-size:11px;line-height:1.45;margin-bottom:16px}
.o-mid .top .win{font-family:"Montserrat",Arial,sans-serif;font-weight:900;font-size:19px;color:var(--lime)}
.o-mid .contact{position:absolute;top:300px;left:0;right:0;text-align:center}
.o-mid .contact .brand{justify-content:center;margin-bottom:28px}
.o-mid .contact h3{font-size:12px;font-weight:800;color:var(--navy);margin-bottom:6px}
.o-mid .contact p{font-size:9px;line-height:1.5}
.o-mid .contact .phone{font-family:"Montserrat",Arial,sans-serif;font-size:14px;font-weight:800;color:var(--navy);margin:10px 0 2px}
.o-mid .foot{position:absolute;bottom:14px;left:0;right:0;display:flex;justify-content:center;color:var(--navy)}

/* outer: cover */
.o-cover .logo-bar{position:absolute;top:20px;left:26px;right:-10px;height:40px;background:var(--navy);border-radius:20px 0 0 20px;padding:12px 0 0 24px}
.o-cover .portrait{top:78px;left:0;right:0;height:200px;background:linear-gradient(160deg,#e4e2e6,#b6aeb0 60%,#8b7f84)}
.o-cover .title{position:absolute;top:282px;right:18px;text-align:right;font-family:"Montserrat",Arial,sans-serif;font-weight:900;color:var(--navy);line-height:1.05}
.o-cover .title .l1{font-size:26px}
.o-cover .title .amp{color:var(--lime);font-size:28px}
.o-cover .title .l2{font-size:17px}
.o-cover .title .l3{font-size:26px}
.o-cover .foot{position:absolute;bottom:0;left:0;right:0;height:70px;padding:30px 16px 0;display:flex;justify-content:space-between;color:var(--white);font-size:10px;font-weight:700}

/* inner: left */
.i-left{padding:18px 18px 0}
.i-left h2{font-size:12px;font-weight:800;color:var(--navy);border-bottom:2px solid var(--lime);padding-bottom:3px;margin-bottom:6px}
.i-left p.body{font-size:9px;line-height:1.45;margin-bottom:12px}
.i-left .ticks li{font-size:9.5px}
.i-left .tag{font-family:"Montserrat",Arial,sans-serif;font-weight:800;font-size:12px;color:var(--lime);margin-top:8px;line-height:1.3}
.i-left .tag span{color:var(--navy)}
.i-left .truck{top:290px;left:0;width:180px;height:110px;background:linear-gradient(135deg,#f2f2f4,#b9bcc6 60%,#6f7385);border-radius:0 55px 55px 0}
.i-left .services{position:absolute;bottom:0;left:0;right:0;height:110px;padding:38px 20px 0;color:var(--white)}
.i-left .services h3{font-size:20px;font-weight:900;color:var(--lime)}
.i-left .services p{font-size:10px;line-height:1.4}

/* inner: middle */
.i-mid{padding:18px 16px 0}
.i-mid h2{font-size:12px;font-weight:800;color:var(--navy);border-bottom:2px solid var(--lime);padding-bottom:3px;margin-bottom:6px}
.i-mid p.body{font-size:9px;line-height:1.45;margin-bottom:10px}
.i-mid .quote{width:122px;font-family:"Montserrat",Arial,sans-serif;font-size:14px;font-weight:800;color:var(--lime);line-height:1.25}
.i-mid .quote b{color:var(--navy);font-weight:900}
.i-mid .photo-a{top:104px;right:0;width:104px;height:112px;border-radius:0 0 0 40px;background:linear-gradient(150deg,#d8d6dc,#8d8b9b)}
.i-mid .photo-b{top:236px;left:16px;width:170px;height:88px;border-radius:8px;background:linear-gradient(140deg,#eeeef2,#a3a5b3 70%,#5f6275)}
.i-mid .lower{position:absolute;bottom:0;left:0;right:0;height:205px;padding:56px 18px 0}
.i-mid .lower p{font-size:10px;line-height:1.4;margin-bottom:10px}
.i-mid .lower .ticks li{font-size:10px}

/* inner: right */
.i-right .photo-c{top:0;left:0;right:0;height:180px;background:linear-gradient(160deg,#ebe6e2,#c3b3a9 60%,#907d76)}
.i-right .photo-d{top:190px;left:14px;width:100px;height:90px;border-radius:50%;background:linear-gradient(140deg,#d6d5dc,#80828f)}
.i-right .photo-e{top:200px;left:118px;width:120px;height:110px;border-radius:50%;background:linear-gradient(140deg,#e5e3e8,#9a97a6)}
.i-right .lower{position:absolute;bottom:0;left:0;right:0;height:205px;padding:56px 20px 0}
.i-right .lower p{font-size:10.5px;line-height:1.4;font-weight:600;margin-bottom:10px}
.i-right .lower .ticks li{font-size:10px}
</style>
</head>
<body>

<section class="spread spread--outer" aria-label="Brochure outside">

  <article class="panel o-left">
    <div class="intro dark">
      <p>Our team of improvement professionals will help you with the ones that mean the most to you!</p>
      <ul class="ticks">
        <li>Higher on-time delivery</li>
        <li>Lower Exchanges or Damages</li>
        <li>Greater Customer Satisfaction</li>
      </ul>
    </div>
    <svg class="swoosh" style="top:175px" width="254" height="60" viewBox="0 0 254 60" aria-hidden="true">
      <path d="M0 30 Q127 70 254 10 L254 0 L0 0 Z" fill="var(--navy)"/>
      <path d="M0 36 Q127 78 254 16" fill="none" stroke="var(--lime)" stroke-width="4"/>
    </svg>
    <div class="team">
      <h3>At BRAVECREST TEAM We:</h3>
      <ul class="ticks">
        <li>Practice a simple no-nonsense approach to problem solving</li>
        <li>Are efficient, resourceful and thorough</li>
      </ul>
    </div>
    <div class="help">
      <div class="small">WE'RE HERE TO</div>
      <div class="big">HELP YOU</div>
      <div class="small">IMPROVE YOUR</div>
      <div class="under">BOTTOM LINE</div>
    </div>
    <svg class="swoosh" style="bottom:0" width="254" height="80" viewBox="0 0 254 80" aria-hidden="true">
      <path d="M0 30 Q140 0 254 40 L254 80 L0 80 Z" fill="var(--navy)"/>
      <path d="M0 22 Q140 -6 254 32" fill="none" stroke="var(--lime)" stroke-width="4"/>
    </svg>
    <div class="foot web">
      <svg width="12" height="12" viewBox="0 0 12 12" aria-hidden="true"><circle cx="6" cy="6" r="5" fill="none" stroke="var(--lime)" stroke-width="1.4"/><path d="M1 6h10M6 1c-3 3-3 7 0 10M6 1c3 3 3 7 0 10" fill="none" stroke="var(--lime)" stroke-width="1"/></svg>
      www.bravecrest-3pl.com
    </div>
  </article>

  <article class="panel o-mid">
    <div class="top dark">
      <p>Bravecrest is what happens when you get moving …</p>
      <p>Building success is following one win immediately with another.</p>
      <div class="win">WHEN YOU WIN<br>WE WIN!</div>
    </div>
    <svg class="swoosh" style="top:225px" width="254" height="60" viewBox="0 0 254 60" aria-hidden="true">
      <path d="M0 10 Q127 70 254 10 L254 0 L0 0 Z" fill="var(--navy)"/>
      <path d="M0 16 Q127 78 254 16" fill="none" stroke="var(--lime)" stroke-width="4"/>
    </svg>
    <div class="contact">
      <div class="brand brand--navy"><span class="dot"></span>BRAVECREST 3PL</div>
      <h3>CONTACT US</h3>
      <p><b>Corporate Office</b></p>
      <p>Bravecrest 3PL<br>2480 Harbor Point Blvd, Suite 210<br>Fairhaven, CA 90814</p>
      <div class="phone">(415) 273-6150</div>
      <p>info@bravecrest-3pl.com</p>
    </div>
    <div class="foot web">
      <svg width="12" height="12" viewBox="0 0 12 12" aria-hidden="true"><circle cx="6" cy="6" r="5" fill="none" stroke="var(--lime)" stroke-width="1.4"/><path d="M1 6h10M6 1c-3 3-3 7 0 10M6 1c3 3 3 7 0 10" fill="none" stroke="var(--lime)" stroke-width="1"/></svg>
      www.bravecrest-3pl.com
    </div>
  </article>

  <article class="panel o-cover">
    <div class="logo-bar"><div class="brand"><span class="dot"></span>BRAVECREST 3PL</div></div>
    <div class="photo portrait" role="img" aria-label="Photo of a smiling customer service agent wearing a headset"></div>
    <svg class="swoosh" style="top:200px" width="254" height="110" viewBox="0 0 254 110" aria-hidden="true">
      <path d="M0 30 Q100 90 254 40 L254 110 L0 110 Z" fill="var(--white)"/>
      <path d="M0 22 Q100 82 254 32" fill="none" stroke="var(--lime)" stroke-width="4"/>
    </svg>
    <div class="title">
      <div class="l1">HOME <span class="amp">&amp;</span></div>
      <div class="l2">DELIVERY</div>
      <div class="l3">ASSEMBLY</div>
    </div>
    <svg class="swoosh" style="bottom:0" width="254" height="110" viewBox="0 0 254 110" aria-hidden="true">
      <path d="M0 50 Q120 10 254 30 L254 110 L0 110 Z" fill="var(--lime)"/>
      <path d="M0 62 Q120 26 254 44 L254 110 L0 110 Z" fill="var(--navy)"/>
    </svg>
    <div class="foot">
      <span>(415) 273-6150</span>
      <span>www.bravecrest-3pl.com</span>
    </div>
  </article>
</section>

<section class="spread spread--inner" aria-label="Brochure inside">

  <article class="panel i-left">
    <h2>ABOUT US</h2>
    <p class="body">We are a 3rd Party Logistics company specializing in home delivery and assembly for the home furnishings market.</p>
    <h2>OUR JOB</h2>
    <ul class="ticks">
      <li>Create Satisfied Customers</li>
      <li>Responsible Handling of Your Merchandise</li>
      <li>Represent You Professionally</li>
    </ul>
    <div class="tag">Bravecrest is what happens<br><span>when you get moving …</span></div>
    <div class="photo truck" role="img" aria-label="Photo of a white box delivery truck"></div>
    <svg class="swoosh" style="bottom:0" width="254" height="150" viewBox="0 0 254 150" aria-hidden="true">
      <path d="M0 60 Q130 20 254 0 L254 150 L0 150 Z" fill="var(--navy)"/>
      <path d="M0 50 Q130 10 254 -10" fill="none" stroke="var(--lime)" stroke-width="5"/>
    </svg>
    <div class="services">
      <h3>SERVICES</h3>
      <p>We're Here To Help You<br>Improve Your Bottom Line</p>
    </div>
  </article>

  <article class="panel i-mid">
    <h2>OUR MISSION…</h2>
    <p class="body">Provide a simple, dependable delivery experience to every customer.</p>
    <div class="quote">Building success<br>is following one<br><b>WIN</b><br>immediately<br>with<br>another.</div>
    <div class="photo photo-a" role="img" aria-label="Photo of delivery crew carrying furniture"></div>
    <div class="photo photo-b" role="img" aria-label="Photo of technicians assembling furniture in a home"></div>
    <svg class="swoosh" style="bottom:0" width="254" height="240" viewBox="0 0 254 240" aria-hidden="true">
      <path d="M0 30 Q120 70 254 20 L254 240 L0 240 Z" fill="var(--navy)"/>
      <path d="M0 22 Q120 62 254 12" fill="none" stroke="var(--lime)" stroke-width="5"/>
    </svg>
    <div class="lower" style="color:var(--white)">
      <p>Bravecrest Provides<br>Home Delivery &amp; Assembly<br>Solutions for Southern California</p>
      <ul class="ticks">
        <li>Dining Room &amp; Living Room Furniture</li>
        <li>Appliances</li>
        <li>Mattress &amp; Bedroom Sets</li>
      </ul>
    </div>
  </article>

  <article class="panel i-right">
    <div class="photo photo-c" role="img" aria-label="Photo of a happy customer at home"></div>
    <svg class="swoosh" style="top:150px" width="254" height="50" viewBox="0 0 254 50" aria-hidden="true">
      <path d="M0 40 Q130 0 254 20 L254 50 L0 50 Z" fill="var(--white)"/>
      <path d="M0 34 Q130 -6 254 14" fill="none" stroke="var(--lime)" stroke-width="4"/>
    </svg>
    <div class="photo photo-d" role="img" aria-label="Photo of delivery team unloading boxes"></div>
    <div class="photo photo-e" role="img" aria-label="Photo of appliance installation"></div>
    <svg class="swoosh" style="bottom:0" width="254" height="240" viewBox="0 0 254 240" aria-hidden="true">
      <path d="M0 20 Q130 70 254 30 L254 240 L0 240 Z" fill="var(--navy)"/>
      <path d="M0 12 Q130 62 254 22" fill="none" stroke="var(--lime)" stroke-width="5"/>
    </svg>
    <div class="lower" style="color:var(--white)">
      <p>Our Team Will Help You<br>With The Areas That Mean The<br>Most To Your Business</p>
      <ul class="ticks">
        <li>Timely Delivery</li>
        <li>Handle Your Merchandise With Care</li>
        <li>Creating Satisfied Customers</li>
      </ul>
    </div>
  </article>
</section>

</body>
</html>
```